Havenmark Electrical Business Card

create a simple but clear business card and letterhead - needs to be professional not too fancy and direct.

Target Market(s)

Home builders

Contact Information for Business Card

Information needed
Havenmark Electrical Contracting
EC. No. 418237
Derek Hollowell
Mobile 0437215609
derek@havenmarkelectrical.com.au

Requirements
Must have
• logo
• Havenmark Electrical Contracting - H.E.C.
• EC. No. 418237
• Derek Hollowell
• Mobile 0437215609
• derek@havenmarkelectrical.com.au
Nice to have
• black with white printing simple but clear
Should not have
• too much information
• no fancy writing

```html
<!DOCTYPE html>
<html lang="en">
<head>
<meta charset="utf-8">
<title>Havenmark Electrical Contracting – Business Card</title>
<link href="https://fonts.googleapis.com/css2?family=Arimo:wght@400;700&display=swap" rel="stylesheet">
<style>
  :root {
    --backdrop: #e9e7e3;
    --card: #ffffff;
    --ink: #111111;
    --gold: #a8872f;
    --rule: #222222;
    --band-text: #ffffff;
  }
  html, body {
    margin: 0;
    width: 1200px;
    height: 902px;
    overflow: hidden;
    background: var(--backdrop);
    font-family: "Arimo", Arial, sans-serif;
  }
  .business-card {
    position: absolute;
    left: 100px;
    top: 166px;
    width: 1000px;
    height: 570px;
    background: var(--card);
    box-shadow: 0 6px 24px rgba(0,0,0,0.15);
    overflow: hidden;
    color: var(--ink);
  }
  .brand {
    position: absolute;
    left: 60px;
    top: 50px;
    display: flex;
    align-items: center;
    gap: 28px;
  }
  .brand-mark {
    width: 130px;
    height: 130px;
    border-radius: 50%;
    background: var(--ink);
  }
  .brand-name {
    font-weight: 700;
    color: var(--ink);
    line-height: 1.05;
  }
  .brand-name .line-main {
    display: block;
    font-size: 66px;
    letter-spacing: 2px;
    text-transform: uppercase;
  }
  .brand-name .line-sub {
    display: block;
    font-size: 34px;
    letter-spacing: 1px;
  }
  .holder-name {
    position: absolute;
    left: 60px;
    top: 285px;
    margin: 0;
    font-size: 50px;
    font-weight: 400;
    color: var(--gold);
  }
  .divider {
    position: absolute;
    left: 560px;
    top: 218px;
    width: 2px;
    height: 145px;
    background: var(--rule);
  }
  .contact-list {
    position: absolute;
    left: 592px;
    top: 215px;
    margin: 0;
    padding: 0;
    list-style: none;
    font-size: 20px;
    line-height: 1.25;
  }
  .contact-list li {
    display: flex;
    align-items: flex-start;
    gap: 14px;
    margin-bottom: 8px;
  }
  .contact-icon {
    flex: 0 0 22px;
    width: 22px;
    height: 22px;
    margin-top: 2px;
  }
  .band {
    position: absolute;
    left: 0;
    top: 0;
  }
  .band-caption {
    font-family: "Arimo", Arial, sans-serif;
    font-size: 21px;
    fill: var(--band-text);
  }
</style>
</head>
<body>
  <section class="business-card">
    <div class="brand">
      <div class="brand-mark"></div>
      <div class="brand-name">
        <span class="line-main">Havenmark</span>
        <span class="line-sub">Electrical Contracting</span>
      </div>
    </div>

    <h1 class="holder-name">Derek Hollowell</h1>

    <div class="divider"></div>

    <ul class="contact-list">
      <li>
        <svg class="contact-icon" viewBox="0 0 22 22"><rect width="22" height="22" fill="#a8872f"/><path d="M7 5l3 3-1.5 1.5a8 8 0 0 0 4 4L14 12l3 3-2 2c-5 0-10-5-10-10z" fill="#fff"/></svg>
        <span>0437215609</span>
      </li>
      <li>
        <svg class="contact-icon" viewBox="0 0 22 22"><rect width="22" height="22" fill="#a8872f"/><rect x="5" y="7" width="12" height="8" fill="none" stroke="#fff" stroke-width="1.5"/><path d="M5 7l6 5 6-5" fill="none" stroke="#fff" stroke-width="1.5"/></svg>
        <span>derek@havenmarkelectrical.com.au</span>
      </li>
      <li>
        <svg class="contact-icon" viewBox="0 0 22 22"><rect width="22" height="22" fill="#a8872f"/><path d="M11 4a5 5 0 0 0-5 5c0 4 5 9 5 9s5-5 5-9a5 5 0 0 0-5-5z" fill="#fff"/><circle cx="11" cy="9" r="2" fill="#a8872f"/></svg>
        <span>14 Larkspur Road<br>BRAMLEY WA 6071<br>EC. No. 418237</span>
      </li>
    </ul>

    <svg class="band" width="1000" height="570" viewBox="0 0 1000 570">
      <path d="M180 500 Q 560 440 1000 385" fill="none" stroke="#111" stroke-width="4" stroke-dasharray="70 8"/>
      <path d="M0 548 Q 540 470 1000 405 L1000 490 Q 560 545 0 570 Z" fill="#111"/>
      <path id="band-curve" d="M120 560 Q 560 505 980 455" fill="none"/>
      <text class="band-caption"><textPath href="#band-curve">Domestic Airconditioning Installation Commercial Phones and Data Points</textPath></text>
    </svg>
  </section>
</body>
</html>
```